Multi App design - layout and graphic suggestions to our new app

Update:
Making a modern and futuristic design of a multifunctional app.
Attached is a description of some of the functionalities.
We need this innovative elegant design on buttons, menu, screens and other elements to be applied onto several mobile screens to choose a style that can be chosen.
Future apps will even include robot assistance, new navigation logic and 3Dish style and several templates to variate the style (look and feel).
Looking forward to see some really new style of futuristic apps!
(We like the app vupa.com - although our design shall be even more modern and creative)

Multi-function app

We would like to have a design suggestion for a multi-function app.

The design shall show front end design as well as navigation and UI/UX user interface

It’s and generic shopping app enabling a long list of services where end user get a menu which is graphical and can be extended with new services as well as customized by end user.
Each service contains functionality as well as content and findings.
Among 5-10 initial services are:

• Shopping assistant and Travel assistant – finding relevant shops/museum and products nearby – sorted by Geofence and Beacons for presenting information - or find stores and experiences
• Loyalty points / Contests and bonus points - preferences and sharing reviews 
• QR and Barcode reader – for increased information
• Campaigns
• Support and feedback

Flexible application - with simple possibility to add new services and allow the user to control the order of the menu / own top menu
Simpler social sharing - reviews, feedback, loyalty points across shops etc.
Easy user management - turn off shops or functionality - without uninstalling

Target Market(s)

End user

Industry/Entity Type

Inn

Requirements
Must have
• The design shall show front end design as well as navigation and UI/UX user interface.
• Attached is your logo and colors with codes

```html
<!DOCTYPE html>
<html lang="en">
<head>
<meta charset="utf-8">
<title>Lumora – Home</title>
<link rel="stylesheet" href="https://fonts.googleapis.com/css2?family=Roboto:wght@400;500&display=swap">
<style>
  :root {
    --backdrop: #5ccaf8;
    --brand: #34c1f6;
    --icon: #1aa9ea;
    --surface: #ececec;
    --tile: #ffffff;
    --ink: #333333;
    --muted: #9a9a9a;
    --dashboard: #3b7fc3;
    --pink: #ec2a8d;
    --photo-top: #3b3430;
    --photo-bottom: #2a2320;
    --divider: #d4d4d4;
  }
  * { box-sizing: border-box; margin: 0; padding: 0; }
  html, body {
    width: 1200px; height: 800px; overflow: hidden;
    background: var(--backdrop);
    font-family: "Roboto", Helvetica, Arial, sans-serif;
    color: var(--ink);
  }
  .stage { width: 1200px; height: 800px; display: flex; align-items: center; justify-content: center; }
  .screen {
    width: 312px; height: 554px;
    background: var(--surface);
    display: flex; flex-direction: column;
    transform: scale(1.38);
    box-shadow: 0 6px 20px rgba(0,0,0,.12);
    overflow: hidden;
  }

  .status-bar {
    height: 16px; background: var(--brand); color: #fff;
    font-size: 7.5px; display: flex; align-items: center; justify-content: space-between;
    padding: 0 6px;
  }
  .status-left, .status-right { display: flex; align-items: center; gap: 4px; width: 80px; }
  .status-right { justify-content: flex-end; }
  .battery { width: 16px; height: 7px; border: 1px solid #fff; border-radius: 1px; padding: 1px; }
  .battery span { display: block; width: 80%; height: 100%; background: #fff; }

  .app-bar {
    height: 32px; background: var(--brand); color: #fff;
    display: flex; align-items: center; justify-content: center; position: relative;
    font-size: 12px;
  }
  .app-bar .menu-btn { position: absolute; left: 7px; top: 8px; }

  .content { flex: 1; padding: 7px 8px 0; }

  .category-grid { display: grid; grid-template-columns: 1fr 1fr; gap: 7px 9px; }
  .category {
    height: 80px; background: var(--tile); border-radius: 3px;
    box-shadow: 0 1px 2px rgba(0,0,0,.15);
    display: flex; flex-direction: column; align-items: center; justify-content: flex-end;
    padding-bottom: 13px; gap: 6px; font-size: 12px;
  }

  .quick-actions { display: grid; grid-template-columns: 1fr 1fr; gap: 9px; margin: 7px 0; }
  .pill {
    height: 34px; border-radius: 17px; color: #fff; font-size: 13px;
    display: flex; align-items: center; justify-content: center;
  }
  .pill.dashboard { background: var(--dashboard); }
  .pill.mini-shop { background: var(--pink); }

  .guide-grid { display: grid; grid-template-columns: repeat(3, 1fr); gap: 7px 5px; }
  .guide {
    background: var(--tile); border-radius: 3px; overflow: hidden;
    box-shadow: 0 1px 2px rgba(0,0,0,.15); height: 116px;
  }
  .guide-photo {
    height: 77px; color: #fff; text-align: center; padding-top: 19px;
    background: linear-gradient(180deg, var(--photo-top), var(--photo-bottom));
  }
  .guide-city { font-size: 11.5px; letter-spacing: .1px; }
  .guide-title { font-size: 8.5px; line-height: 10px; margin-top: 3px; }
  .guide-author { display: flex; align-items: center; gap: 5px; padding: 6px 3px; }
  .avatar { width: 24px; height: 24px; border-radius: 50%; background: linear-gradient(135deg, #6b5446, #2e241f); flex: none; }
  .author-name { font-size: 8.5px; line-height: 11px; }
  .author-role { font-size: 8.5px; color: var(--muted); line-height: 11px; }

  .tab-bar {
    height: 37px; background: #fff; border-top: 1px solid var(--divider);
    display: grid; grid-template-columns: repeat(5, 1fr);
  }
  .tab {
    display: flex; flex-direction: column; align-items: center; justify-content: center;
    gap: 2px; font-size: 8px; color: #555; border-left: 1px solid var(--divider);
  }
  .tab:first-child { border-left: none; }
</style>
</head>
<body>
<main class="stage">
  <section class="screen">
    <div class="status-bar">
      <div class="status-left">●●●○○ Nimbo
        <svg width="9" height="7" viewBox="0 0 9 7"><path d="M.5 2.5a5.6 5.6 0 0 1 8 0M2 4a3.5 3.5 0 0 1 5 0" stroke="#fff" fill="none"/><circle cx="4.5" cy="5.8" r=".9" fill="#fff"/></svg>
      </div>
      <div>12:37 pm</div>
      <div class="status-right">80% <div class="battery"><span></span></div></div>
    </div>

    <header class="app-bar">
      <svg class="menu-btn" width="22" height="16" viewBox="0 0 22 16"><path d="M0 1.5h22M0 8h22M0 14.5h22" stroke="#fff" stroke-width="2"/></svg>
      Lumora
    </header>

    <div class="content">
      <nav class="category-grid">
        <div class="category">
          <svg width="52" height="32" viewBox="0 0 52 32" fill="var(--icon)">
            <path d="M3 2v9a3 3 0 0 0 2 3v16h3V14a3 3 0 0 0 2-3V2H9v8H8V2H6v8H5V2z"/>
            <circle cx="26" cy="16" r="15"/><circle cx="26" cy="16" r="12.5" fill="none" stroke="#fff" stroke-width="1.2"/>
            <path d="M45 2c3 3 4 9 2 13l-1 1v14h-3V2z"/>
          </svg>
          Restaurants
        </div>
        <div class="category">
          <svg width="38" height="38" viewBox="0 0 38 38" fill="none" stroke="var(--icon)" stroke-width="2">
            <path d="M3 2h17v7a8.5 8.5 0 0 1-17 0z" fill="#fff"/><path d="M3.5 9h16" /><path d="M4 10a7.5 7.5 0 0 0 15 0z" fill="var(--icon)"/>
            <path d="M11.5 18v17M6 36h11"/>
            <path d="M16 14h20l-10 11z" fill="#fff"/><path d="M26 25v10M21 36h10"/>
          </svg>
          Nightclubs
        </div>
        <div class="category">
          <svg width="38" height="30" viewBox="0 0 38 30" fill="var(--icon)">
            <rect x="1" y="6" width="36" height="23" rx="3"/><rect x="4" y="3" width="6" height="4"/><rect x="13" y="2" width="12" height="6" rx="1"/>
            <circle cx="21" cy="17.5" r="8" fill="#fff"/><circle cx="21" cy="17.5" r="5.5"/><circle cx="21" cy="17.5" r="3.5" fill="#fff"/>
            <rect x="4" y="10" width="5" height="3" fill="#fff"/>
          </svg>
          Attractions
        </div>
        <div class="category">
          <svg width="38" height="32" viewBox="0 0 38 32" fill="var(--icon)">
            <path d="M13 11l6-9 6 9" fill="none" stroke="var(--icon)" stroke-width="2.5"/>
            <rect x="1" y="10" width="36" height="6"/><path d="M3 18h32l-2 13H5z"/>
          </svg>
          Shopping
        </div>
      </nav>

      <div class="quick-actions">
        <div class="pill dashboard">Status/Dashboard</div>
        <div class="pill mini-shop">Min Shopping App</div>
      </div>

      <div class="guide-grid">
        <article class="guide"><div class="guide-photo" role="img" aria-label="Photo of a vintage clothing store"><div class="guide-city">LOS ANGELES</div><div class="guide-title">Vintage Shopping<br>in L.A</div></div><div class="guide-author"><div class="avatar" role="img" aria-label="Guide portrait"></div><div><div class="author-name">Mara Ellison</div><div class="author-role">Vintage Expert</div></div></div></article>
        <article class="guide"><div class="guide-photo" role="img" aria-label="Photo of a vintage clothing store"><div class="guide-city">LOS ANGELES</div><div class="guide-title">Vintage Shopping<br>in L.A</div></div><div class="guide-author"><div class="avatar" role="img" aria-label="Guide portrait"></div><div><div class="author-name">Mara Ellison</div><div class="author-role">Vintage Expert</div></div></div></article>
        <article class="guide"><div class="guide-photo" role="img" aria-label="Photo of a vintage clothing store"><div class="guide-city">LOS ANGELES</div><div class="guide-title">Vintage Shopping<br>in L.A</div></div><div class="guide-author"><div class="avatar" role="img" aria-label="Guide portrait"></div><div><div class="author-name">Mara Ellison</div><div class="author-role">Vintage Expert</div></div></div></article>
        <article class="guide"><div class="guide-photo" role="img" aria-label="Photo of a vintage clothing store"><div class="guide-city">LOS ANGELES</div><div class="guide-title">Vintage Shopping<br>in L.A</div></div><div class="guide-author"><div class="avatar" role="img" aria-label="Guide portrait"></div><div><div class="author-name">Mara Ellison</div><div class="author-role">Vintage Expert</div></div></div></article>
        <article class="guide"><div class="guide-photo" role="img" aria-label="Photo of a vintage clothing store"><div class="guide-city">LOS ANGELES</div><div class="guide-title">Vintage Shopping<br>in L.A</div></div><div class="guide-author"><div class="avatar" role="img" aria-label="Guide portrait"></div><div><div class="author-name">Mara Ellison</div><div class="author-role">Vintage Expert</div></div></div></article>
        <article class="guide"><div class="guide-photo" role="img" aria-label="Photo of a vintage clothing store"><div class="guide-city">LOS ANGELES</div><div class="guide-title">Vintage Shopping<br>in L.A</div></div><div class="guide-author"><div class="avatar" role="img" aria-label="Guide portrait"></div><div><div class="author-name">Mara Ellison</div><div class="author-role">Vintage Expert</div></div></div></article>
      </div>
    </div>

    <nav class="tab-bar">
      <div class="tab">
        <svg width="13" height="11" viewBox="0 0 13 11" fill="none" stroke="#444"><rect x="1" y="4" width="11" height="6.5"/><path d="M.5 4L2 .5h9L12.5 4z" fill="#444"/><rect x="5" y="6.5" width="3" height="4"/></svg>Shop
      </div>
      <div class="tab">
        <svg width="13" height="13" viewBox="0 0 13 13"><circle cx="6.5" cy="6.5" r="4.5" fill="none" stroke="#444" stroke-width="2.4" stroke-dasharray="2 1.5"/><circle cx="6.5" cy="6.5" r="3.5" fill="none" stroke="#444" stroke-width="1.4"/></svg>Services
      </div>
      <div class="tab">
        <svg width="16" height="11" viewBox="0 0 16 11" fill="none" stroke="#444" stroke-width="1.3"><path d="M1.5 10a6.5 6.5 0 1 1 13 0"/><path d="M8 10l3-4"/><path d="M3 10h10"/></svg>Dashboard
      </div>
      <div class="tab">
        <svg width="13" height="13" viewBox="0 0 13 13" fill="none" stroke="#444" stroke-width="1.4"><circle cx="5" cy="5" r="4"/><path d="M8 8l4.5 4.5"/></svg>Search
      </div>
      <div class="tab">
        <svg width="22" height="14" viewBox="0 0 22 14"><path d="M0 1h22M0 7h22M0 13h22" stroke="#333" stroke-width="1.6"/></svg>
      </div>
    </nav>
  </section>
</main>
</body>
</html>
```